Real Estate Business Card

On the front side I want to have my info, my brokerage info.
On the back side I want have my complany’s logo, website and Facebook link. I will provide all this once I select a design.

I would like to see Black background and gold text, Dark Blue and gold text and White and blue text designs

Font styles to use
Sans Serif
Script

```html
<!DOCTYPE html>
<html lang="en">
<head>
<meta charset="utf-8">
<title>Ironpeak Real Estate – Business Card</title>
<link href="https://fonts.googleapis.com/css2?family=Roboto:wght@400;500;700;900&display=swap" rel="stylesheet">
<style>
  :root {
    --backdrop: #2a2a2c;
    --card: #1e1e20;
    --gold: #d9b24a;
    --red: #d8343a;
    --slate: #7f8aa3;
    --white: #f1f1f1;
    --rule: #9a9a9a;
  }
  * { box-sizing: border-box; margin: 0; padding: 0; }
  html, body {
    width: 1200px; height: 900px; overflow: hidden;
    background: var(--backdrop);
    font-family: "Roboto", Arial, sans-serif;
  }
  .card {
    position: absolute; left: 240px;
    width: 720px; height: 400px;
    background: var(--card);
    box-shadow: 0 8px 24px rgba(0,0,0,.45);
    overflow: hidden;
  }
  .card--logo { top: 35px; display: flex; align-items: center; justify-content: center; }
  .card--info { top: 465px; }

  .brand { display: flex; align-items: center; gap: 14px; color: var(--red); font-weight: 900; }
  .brand__square { width: 46px; height: 46px; background: var(--red); }
  .brand__name { font-size: 40px; letter-spacing: 1px; text-transform: uppercase; }

  .card--info .brand { position: absolute; right: 32px; top: 120px; gap: 10px; }
  .card--info .brand__square { width: 30px; height: 30px; }
  .card--info .brand__name { font-size: 30px; }

  .person { position: absolute; left: 40px; top: 212px; }
  .person__name { color: var(--gold); font-size: 26px; font-weight: 700; letter-spacing: .5px; }
  .person__title { color: var(--red); font-size: 17px; font-weight: 500; margin-top: 2px; }

  .divider { position: absolute; left: 40px; right: 32px; top: 276px; height: 1px; background: var(--rule); }

  .contacts { position: absolute; left: 40px; top: 290px; list-style: none; }
  .contacts li { display: flex; align-items: center; gap: 12px; color: var(--white); font-size: 17px; height: 23px; }
  .contacts svg { width: 15px; height: 15px; fill: var(--gold); flex: none; }

  .address { position: absolute; right: 32px; top: 296px; text-align: right; color: var(--white); font-size: 18px; font-weight: 500; line-height: 24px; }

  .stripe { position: absolute; bottom: 0; height: 11px; }
  .stripe--red { left: 0; width: 540px; background: var(--red); }
  .stripe--slate { left: 546px; right: 0; background: var(--slate); }
</style>
</head>
<body>
  <section class="card card--logo">
    <div class="brand">
      <span class="brand__square"></span>
      <span class="brand__name">Ironpeak Real Estate</span>
    </div>
  </section>

  <section class="card card--info">
    <div class="brand">
      <span class="brand__square"></span>
      <span class="brand__name">Ironpeak Real Estate</span>
    </div>

    <div class="person">
      <p class="person__name">DANIEL HART</p>
      <p class="person__title">CEO/FOUNDER</p>
    </div>

    <div class="divider"></div>

    <ul class="contacts">
      <li><svg viewBox="0 0 16 16"><path d="M3.5 1 6 4 4.6 5.6c.8 2 2.6 3.8 4.6 4.6L10.8 9l3 2.5-1.6 2.8C6.8 14 2 9.2 1.7 3.8z"/></svg>555 210 4471</li>
      <li><svg viewBox="0 0 16 16"><path d="M4 0h8v16H4zM5.5 2v10h5V2zM7 13.3h2v1.2H7z" fill-rule="evenodd"/></svg>555 382 9016</li>
      <li><svg viewBox="0 0 16 16"><path d="M4 1h7v4H4zM1 6h14v7h-2v2H3v-2H1zM5 10v3h6v-3z" fill-rule="evenodd"/></svg>555 704 1263</li>
      <li><svg viewBox="0 0 16 16"><path d="M1 3h14v10H1zM2.5 4.5 8 8.5l5.5-4z" fill-rule="evenodd"/></svg>daniel@ironpeakhomes.com</li>
    </ul>

    <address class="address" style="font-style:normal">
      1420 Juniper Court<br>
      Fairbanks, Alaska 99701<br>
      www.ironpeakhomes.com
    </address>

    <div class="stripe stripe--red"></div>
    <div class="stripe stripe--slate"></div>
  </section>
</body>
</html>
```